Salt Moon, Tin Heart

Hey Guys
Please visit our Chatterleaf page for the film. See what ideas you bring to the table for the movie poster.
Looking for creative and something fresh.
Check out cast on QVTK
Will use the stills from the film for actual poster and quality.
Thanks a million for taking an interest in our film. xoxo
Target Market(s)
2-50 year old, date night, girls night out
Industry/Entity Type
Movie

```html
<!DOCTYPE html>
<html lang="en">
<head>
<meta charset="utf-8">
<title>Salt Moon, Tin Heart — Poster</title>
<link rel="stylesheet" href="https://fonts.googleapis.com/css2?family=Open+Sans:wght@400&display=swap">
<style>
  :root {
    --backdrop: #2f2f2f;
    --sky-top: #d6dde2;
    --sky-glow: #ebe2da;
    --sky-dusk: #d9cbc8;
    --sea: #8795a4;
    --surf: #a9b2bc;
    --sand-light: #a4a8ae;
    --sand-dark: #8a919b;
    --ink: #ffffff;
  }
  * { box-sizing: border-box; margin: 0; padding: 0; }
  html, body {
    width: 1200px;
    height: 1200px;
    overflow: hidden;
    background: var(--backdrop);
  }
  .poster {
    position: absolute;
    left: 211px;
    top: 0;
    width: 778px;
    height: 1200px;
    overflow: hidden;
    font-family: "Open Sans", "Myriad Pro", sans-serif;
    color: var(--ink);
  }
  .still {
    position: absolute;
    inset: 0;
    background: linear-gradient(
      to bottom,
      var(--sky-top) 0%,
      var(--sky-glow) 36%,
      var(--sky-dusk) 54%,
      var(--sea) 56.5%,
      var(--surf) 62%,
      var(--sand-light) 66%,
      var(--sand-dark) 100%
    );
  }
  .title {
    position: absolute;
    left: 148px;
    width: 482px;
    top: 0;
  }
  .title-word {
    position: absolute;
    left: 0;
    width: 100%;
    display: flex;
    justify-content: space-between;
    font-size: 122px;
    font-weight: 400;
    line-height: 1;
    text-transform: uppercase;
  }
  .title-word:nth-child(1) { top: 122px; }
  .title-word:nth-child(2) { top: 333px; }
  .title-word:nth-child(3) { top: 544px; }
  .title-word:nth-child(4) { top: 755px; }
  .credits {
    position: absolute;
    left: 0;
    width: 100%;
    top: 1066px;
    text-align: center;
    font-size: 17px;
    line-height: 24px;
    letter-spacing: 2.2px;
  }
</style>
</head>
<body>
  <main class="poster">
    <div class="still" role="img" aria-label="Film still: a couple kissing on a beach at dusk, sea and pale sky behind them"></div>

    <h1 class="title" aria-label="Salt Moon, Tin Heart">
      <span class="title-word"><span>S</span><span>A</span><span>L</span><span>T</span></span>
      <span class="title-word"><span>M</span><span>O</span><span>O</span><span>N</span></span>
      <span class="title-word"><span>T</span><span>I</span><span>N</span></span>
      <span class="title-word"><span>H</span><span>E</span><span>A</span><span>R</span><span>T</span></span>
    </h1>

    <div class="credits">
      <p>Directors: Marla Questov, Tobin Ashgrove Vell</p>
      <p>Writers: Marla Questov (screenplay), Marla Questov</p>
      <p>Stars: Lena Harrow, Reid Castell, Dana Whitcombe</p>
    </div>
  </main>
</body>
</html>
```